Brochure for a website accessibility report

This brochure is related to a report that www.kelvat.org sell. The report shows the results of an automated audit of a websites accessibility. It shows details of issues found with screen shots, examples of code and provides remediation advice.

The brochure will be a pdf 8.5 inches by 11 inches. It can be anywhere from 6 to 10 pages.

The FaultLens™ name itself should be “Bree Serif” font. The fonts, styles, colors and sizes are up to you.

The images used and logo of the Office of Digital Openness and Q7N logo are upload

We highlighted in blue page extracts from the report we sell. Do not use the blue highlight, it is merely there to show you where the specific examples of the report we sell are vs the other content in the report. The areas in blue which show the content from the actual report should be shown as an extract of the actual page of the report. You have flexibility to change the layout and the way the content look.

The red square callouts over the blue content are callouts that describe the specific page extracts. We used it as a red callout only so that you would be able to see it. You should change the specific location, look and feel of the callout to be appropriate

Target Market(s)

Marketing and Technical people

Industry/Entity Type

Information Technology

Font styles to use
Sans Serif

Colors

Designer to choose colors to be used in the design.

Requirements
Should not have
• wheelchairs, images of blind people

```html
<!DOCTYPE html>
<html lang="en">
<head>
<meta charset="utf-8">
<title>Accessibility Report Brochure – Pages 03–04</title>
<link href="https://fonts.googleapis.com/css2?family=Bree+Serif&family=Open+Sans:wght@400;600;700&display=swap" rel="stylesheet">
<style>
  :root{
    --backdrop:#a9abb1;
    --paper:#ffffff;
    --ink:#3a3d42;
    --brand-blue:#1f4fa0;
    --night:#0f1723;
    --night-mid:#23324a;
    --steel:#3d5675;
    --panel:rgba(14,18,26,0.82);
    --panel-text:#e9edf3;
    --rule-light:#dfe3ea;
  }
  *{box-sizing:border-box;margin:0;padding:0}
  html,body{width:1200px;height:900px;overflow:hidden}
  body{background:var(--backdrop);font-family:"Open Sans",Arial,sans-serif;color:var(--ink)}
  .spread{position:absolute;left:190px;top:157px;width:820px;height:587px;display:flex}
  .page{position:relative;width:410px;height:587px;overflow:hidden}

  /* Left page */
  .page--mission{background:var(--paper)}
  .mission-body{position:absolute;left:57px;top:76px;width:326px;font-size:7.6px;line-height:1.42}
  .mission-body p{margin-bottom:9px}
  .partner-mark{display:flex;align-items:center;justify-content:center;gap:6px;margin:8px 0 14px}
  .partner-mark__square{width:14px;height:14px;background:var(--brand-blue)}
  .partner-mark__name{font-family:"Open Sans",Arial,sans-serif;font-weight:700;font-size:20px;color:var(--brand-blue);letter-spacing:1px}
  .principle{margin-bottom:8px}
  .principle h3{font-size:7.8px;font-weight:700;color:var(--brand-blue)}
  .page-footer{position:absolute;bottom:10px;display:flex;align-items:center;font-size:7px;font-variant:small-caps;letter-spacing:.5px}
  .page--mission .page-footer{left:57px;right:0}
  .page-number{font-weight:700;color:var(--brand-blue);padding-right:6px;border-right:1px solid var(--brand-blue);margin-right:6px}
  .footer-title{color:var(--brand-blue);white-space:nowrap}
  .footer-bar{flex:1;height:4px;background:var(--brand-blue);margin-left:10px}

  /* Right page */
  .page--section{background:var(--night)}
  .section-photo{position:absolute;inset:0;background:
      radial-gradient(ellipse at 20% 8%,#8a6a55 0%,rgba(80,60,55,0) 35%),
      radial-gradient(ellipse at 80% 30%,#4c6a8c 0%,rgba(40,60,90,0) 45%),
      radial-gradient(ellipse at 40% 90%,#3b5878 0%,rgba(30,45,70,0) 45%),
      linear-gradient(160deg,#2b2d36 0%,var(--night-mid) 50%,var(--night) 100%)}
  .section-panel{position:absolute;left:55px;top:84px;width:340px;height:453px;background:var(--panel);padding:26px 26px 20px 28px;color:var(--panel-text)}
  .section-title{font-family:"Bree Serif",Georgia,serif;font-size:25px;letter-spacing:3px;color:#fff;font-weight:400}
  .section-rule{width:56px;height:2px;background:#fff;margin:6px 0 16px}
  .section-intro{font-size:7.6px;line-height:1.42;margin-bottom:9px}
  .summary-table{width:100%;border-collapse:collapse;font-size:5.6px;margin-top:8px;color:#fff}
  .summary-table th{font-size:6.6px;font-weight:600;padding:3px 2px;border:1px solid var(--rule-light)}
  .summary-table td{padding:2.4px 3px;border-bottom:1px solid rgba(223,227,234,.45)}
  .summary-table td.principle-name{font-size:7px;font-weight:600;text-align:center;border:1px solid var(--rule-light)}
  .summary-table td.guideline{font-weight:600;border-left:1px solid var(--rule-light)}
  .summary-table td.issues{border-right:1px solid var(--rule-light);text-align:center;word-spacing:6px}
  .summary-table td.issues span{text-decoration:underline}
  .page--section .page-footer{left:0;right:12px;color:#fff}
  .footer-line{flex:1;height:3px;background:#fff;margin:0 12px 0 60px;max-width:140px}
  .page--section .footer-title{color:#dfe6f0;margin-left:auto;padding-right:6px;border-right:1px solid #fff;margin-right:6px}
  .page--section .page-number{color:#fff;border:none;padding:0;margin:0}
</style>
</head>
<body>
<main class="spread">
  <section class="page page--mission">
    <div class="mission-body">
      <p>The Americans with Disabilities Act (ADA) is a comprehensive federal civil rights law prohibiting discrimination on the basis of disability, enforced by the Department of Justice (DOJ). The ADA prohibits discriminatory lack of access for individuals with disabilities to goods and services of public services and accommodations. Websites are considered places of public accommodations. The DOJ currently uses WCAG 2.1 Level A/AA as an accepted standard by which to measure a website's accessibility.</p>
      <div class="partner-mark"><span class="partner-mark__square"></span><span class="partner-mark__name">Q7N</span></div>
      <p>WCAG 2.1 Level A/AA consists of 12 guidelines with 50 checkpoints that are organized under four principles:</p>
      <div class="principle"><h3>Principle 1: Perceivable</h3><p>Information and user interface components must be presented to users in ways they can perceive. This means that users must be able to comprehend the information being depicted: it can't be invisible to all their senses.</p></div>
      <div class="principle"><h3>Principle 2: Operable</h3><p>User interface components and navigation must be operable. The interface cannot require interaction that a user cannot perform.</p></div>
      <div class="principle"><h3>Principle 3: Understandable</h3><p>Information and the operation of a user interface must be understandable. Users must be able to understand the information as well as the operation of the user interface.</p></div>
      <div class="principle"><h3>Principle 4: Robust</h3><p>Content must be robust enough that it can be interpreted reliably by a wide variety of user agents, including assistive technologies. As technologies and user agents evolve, the content should remain accessible.</p></div>
      <p>Start your journey to a fully compliant website with FaultLens™. This detailed compliance and remediation report is generated based on scanning your website against hundreds of carefully-crafted rules, logging failures, and then generating feedback and recommendations on how to fix the problems based on our years of experience and proven best practices.</p>
    </div>
    <footer class="page-footer"><span class="page-number">03</span><span class="footer-title">Our Mission and Vision</span><span class="footer-bar"></span></footer>
  </section>

  <section class="page page--section">
    <div class="section-photo" role="img" aria-label="Dark close-up photograph of glowing website source code on a screen"></div>
    <div class="section-panel">
      <h2 class="section-title">SECTION 1</h2>
      <div class="section-rule"></div>
      <p class="section-intro">The first section of the report begins with a Summary Chart that breaks down WCAG 2.1 A/AA issues by principle.</p>
      <p class="section-intro">Example WCAG 2.1 A/AA Summary Chart:<br>Checkpoints with failures detected are identified in the "Issues Discovered" column. The detail behind these failures is available in the next section.</p>
      <table class="summary-table">
        <thead><tr><th>Principle</th><th>Guideline</th><th>Issues Discovered</th></tr></thead>
        <tbody>
          <tr><td class="principle-name" rowspan="4">Perceivable</td><td class="guideline">Guideline 1.1 Text Alternatives</td><td class="issues"><span>1.1.1</span></td></tr>
          <tr><td class="guideline">Guideline 1.2 Time-based Media</td><td class="issues"><span>1.2.1</span> <span>1.2.2</span> <span>1.2.3</span> <span>1.2.4</span> <span>1.2.5</span></td></tr>
          <tr><td class="guideline">Guideline 1.3 Adaptable</td><td class="issues"><span>1.3.1</span> <span>1.3.2</span> <span>1.3.3</span></td></tr>
          <tr><td class="guideline">Guideline 1.4 Distinguishable</td><td class="issues"><span>1.4.1</span> <span>1.4.3</span> <span>1.4.4</span> <span>1.4.11</span></td></tr>
          <tr><td class="principle-name" rowspan="3">Operable</td><td class="guideline">Guideline 2.1 Keyboard Accessible</td><td class="issues"><span>2.1.1</span> <span>2.1.2</span></td></tr>
          <tr><td class="guideline">Guideline 2.2 Enough Time</td><td class="issues"><span>2.2.1</span> <span>2.2.2</span></td></tr>
          <tr><td class="guideline">Guideline 2.4 Navigable</td><td class="issues"><span>2.4.1</span> <span>2.4.2</span> <span>2.4.4</span> <span>2.4.7</span></td></tr>
          <tr><td class="principle-name" rowspan="3">Understandable</td><td class="guideline">Guideline 3.1 Readable</td><td class="issues"><span>3.1.1</span></td></tr>
          <tr><td class="guideline">Guideline 3.2 Predictable</td><td class="issues"><span>3.2.1</span> <span>3.2.2</span></td></tr>
          <tr><td class="guideline">Guideline 3.3 Input Assistance</td><td class="issues"><span>3.3.2</span></td></tr>
          <tr><td class="principle-name">Robust</td><td class="guideline">Guideline 4.1 Compatible</td><td class="issues"><span>4.1.1</span> <span>4.1.2</span></td></tr>
        </tbody>
      </table>
    </div>
    <footer class="page-footer"><span class="footer-line"></span><span class="footer-title">Our Mission and Vision</span><span class="page-number">04</span></footer>
  </section>
</main>
</body>
</html>
```